Design website home page for pathology consulting company

Starting a new consulting company with anatomic pathologists focused on expert diagnosis and second opinions on difficult pathology cases. In the near future we will be incorporating next generation diagnostics for rare diseases of childhood into the business. These include discovery and testing of DNA for mutations.

The company is formed around one of the best known pathologists in the world named Marcus "Buddy" Halvorsen. The name of the company is "BuddyScope"

We had a logo design by Sketchfold - it is great. I will attach file as soon as I have it (contest ending today). Our company is medical, uses microscopes, DNA, probably will focus on childhood diseases but not solely on childhood diseases. we're not particularly conservative, but the customers we want to appeal to include older practicing pathologists as well as patients (sometimes parents) looking for second opinions.

Think a group of expert doctors diagnosing disease through the microscope and through DNA technology, ages ranging from 35-75 all trained by the best pathologist in the world - "Buddy"

We receive glass slides from diseases from patients all over the world from docs who need an expert to tell them what is the diagnosis. So "path to the diagnosis" is also part of the company marketing message.

We want the website design to describe our company but be very simple to find what one is looking for as we will use it as the launch page to:
1) order services
2) check results/reports
3) set up new account
4) speak with one of the pathologists
5) see our test menu
6) access our educational material/webinars

Update - looking for home page design and then finalists will ask for second page design to keep with theme - ok?

Reason: realized this project isn't web design but web home page design - thanks

Reason: Holidays for some in next two weeks

Reason: Hot discussion among collaborators for a few of the submissions. Will provide detail individually this weekend. Thanks so much for all the submissions!

Target Market(s)

Referring pathologists, physicians who want second opinions on pathology disease diagnosis, patients who have had biopsies (either patients themselves or parents of patients), generally high education level

Industry/Entity Type

Marketing

Requirements
Must have
• BuddyScope
Next Generation Pathology Consultants

```html
<!DOCTYPE html>
<html lang="en">
<head>
<meta charset="utf-8">
<title>BuddyScope — Next Generation Pathology Consultants</title>
<link href="https://fonts.googleapis.com/css2?family=Roboto+Condensed:wght@400;700&family=Arimo:ital,wght@1,700&family=Gelasio&family=Open+Sans:wght@400;700&display=swap" rel="stylesheet">
<style>
  :root {
    --brand-blue: #1b8fcf;
    --brand-blue-dark: #176fb0;
    --bar-blue: #1e91d0;
    --tab-grey: #9d9fa3;
    --text-grey: #9a9a9a;
    --logo-grey: #8a8c8f;
    --leaf-green: #5f9a12;
    --page-white: #ffffff;
    --grid-line: #e6eef4;
    --photo-light: #e9eef1;
    --photo-mid: #c9d3d8;
    --social-orange: #e8701f;
    --social-blue: #3b6ea8;
    --social-sky: #2a86c2;
    --social-red: #c4302b;
    --social-cyan: #4bb3dd;
  }
  * { box-sizing: border-box; margin: 0; padding: 0; }
  html, body { width: 1200px; height: 960px; overflow: hidden; background: var(--page-white); }
  .page {
    position: relative; width: 1200px; height: 960px; overflow: hidden;
    background:
      linear-gradient(to bottom, rgba(255,255,255,0) 0, rgba(255,255,255,1) 420px),
      repeating-linear-gradient(to right, var(--grid-line) 0 1px, transparent 1px 14px),
      repeating-linear-gradient(to bottom, var(--grid-line) 0 1px, transparent 1px 14px),
      var(--page-white);
  }
  .topbar {
    position: absolute; left: 0; top: 0; width: 1200px; height: 100px;
    background: var(--bar-blue);
    box-shadow: 0 3px 6px rgba(0,0,0,0.15);
  }
  .main-nav a {
    position: absolute; top: 47px;
    font-family: "Roboto Condensed", sans-serif; font-weight: 700; font-size: 22px;
    color: var(--page-white); text-decoration: none; letter-spacing: -0.3px;
    text-shadow: 0 1px 1px rgba(0,0,0,0.2);
  }
  .brand { position: absolute; left: 38px; top: 166px; width: 262px; text-align: center; }
  .brand-mark {
    width: 124px; height: 124px; margin: 0 auto 6px; border-radius: 50%;
    background: var(--logo-grey);
  }
  .brand-name {
    font-family: "Roboto Condensed", sans-serif; font-weight: 700; font-size: 40px;
    line-height: 1; color: var(--brand-blue-dark);
  }
  .brand-tagline {
    margin-top: 3px;
    font-family: "Open Sans", sans-serif; font-size: 13.5px; color: var(--logo-grey);
  }
  .headline {
    position: absolute; left: 52px; top: 410px;
    font-family: "Arimo", sans-serif; font-style: italic; font-weight: 700; font-size: 38px;
    line-height: 38px; letter-spacing: -1.5px; color: var(--brand-blue);
  }
  .hero-frame {
    position: absolute; left: 322px; top: 136px; width: 843px; height: 354px;
    background: var(--page-white); box-shadow: 0 1px 5px rgba(0,0,0,0.25);
  }
  .hero-photo {
    position: absolute; left: 12px; top: 14px; width: 821px; height: 326px;
    background: linear-gradient(100deg, var(--photo-light) 0%, var(--photo-mid) 50%, #b9c6cc 100%);
  }
  .service-tab {
    position: absolute; top: 530px; height: 53px;
    display: flex; align-items: center; justify-content: space-between;
    padding: 0 12px 0 12px;
    font-family: "Roboto Condensed", sans-serif; font-weight: 700; font-size: 22px;
    color: var(--page-white); letter-spacing: -0.5px;
  }
  .service-tab.is-blue { background: var(--brand-blue); }
  .service-tab.is-grey { background: var(--tab-grey); }
  .service-tab svg { flex: none; }
  .service-copy {
    position: absolute; top: 600px; width: 262px;
    font-family: "Gelasio", serif; font-size: 17.5px; line-height: 30px; color: var(--text-grey);
  }
  .email-field {
    position: absolute; left: 37px; top: 735px; width: 267px; height: 40px;
    border: 1px solid #cfd3d6; border-radius: 3px; background: var(--page-white);
    padding: 0 13px; line-height: 38px;
    font-family: "Open Sans", sans-serif; font-size: 12.5px; color: #b7b7b7; letter-spacing: 0.3px;
  }
  .read-more {
    position: absolute; width: 112px; height: 34px;
    font-family: "Open Sans", sans-serif; font-weight: 700; font-size: 12.5px;
    color: var(--page-white); text-align: center; line-height: 34px; text-decoration: none;
    box-shadow: 0 1px 2px rgba(0,0,0,0.2);
  }
  .read-more.is-green { background: var(--leaf-green); }
  .read-more.is-blue { background: var(--brand-blue); }
  .footer-rule {
    position: absolute; left: 0; top: 906px; width: 916px; height: 4px; background: var(--brand-blue);
  }
  .social-links { position: absolute; left: 962px; top: 896px; display: flex; gap: 5px; }
  .social-links span { width: 31px; height: 31px; border-radius: 4px; display: block; }
</style>
</head>
<body>
<div class="page">
  <header class="topbar">
    <nav class="main-nav">
      <a href="#" style="left:344px">HOME</a>
      <a href="#" style="left:456px">ABOUT US</a>
      <a href="#" style="left:596px">ORDER SERVICES</a>
      <a href="#" style="left:790px">CONTACT US</a>
      <a href="#" style="left:943px">EDUCATIONAL SEMINARS</a>
    </nav>
  </header>

  <div class="brand">
    <div class="brand-mark"></div>
    <div class="brand-name">BuddyScope</div>
    <div class="brand-tagline">Next Generation Pathology Consultants</div>
  </div>

  <h1 class="headline">PATH TO THE<br>DIAGNOSIS</h1>

  <div class="hero-frame">
    <div class="hero-photo" role="img" aria-label="Photo of a team of five pathologists in white coats and scrubs"></div>
  </div>

  <div class="service-tab is-blue" style="left:35px;width:282px">
    <span>SET UP AN ACCOUNT</span>
    <svg width="34" height="34" viewBox="0 0 34 34" aria-hidden="true">
      <rect x="2" y="2" width="30" height="30" rx="3" fill="none" stroke="#fff" stroke-width="2.5"/>
      <circle cx="17" cy="13" r="5" fill="#fff"/>
      <path d="M8 28c1-6 5-8 9-8s8 2 9 8z" fill="#fff"/>
    </svg>
  </div>
  <div class="service-tab is-grey" style="left:317px;width:283px">
    <span>CHECK YOUR RESULTS</span>
    <svg width="46" height="28" viewBox="0 0 46 28" aria-hidden="true">
      <polyline points="2,12 8,24 14,10 20,24 26,8 32,22 44,3" fill="none" stroke="#fff" stroke-width="3" stroke-linejoin="round"/>
    </svg>
  </div>
  <div class="service-tab is-blue" style="left:600px;width:284px">
    <span>SEE OUR TEST MENU</span>
    <svg width="28" height="34" viewBox="0 0 28 34" aria-hidden="true">
      <rect x="1" y="3" width="26" height="30" rx="2" fill="#fff"/>
      <rect x="8" y="0" width="12" height="5" rx="1" fill="#fff"/>
      <g stroke="#1b8fcf" stroke-width="2"><line x1="6" y1="12" x2="22" y2="12"/><line x1="6" y1="17" x2="22" y2="17"/><line x1="6" y1="22" x2="22" y2="22"/><line x1="6" y1="27" x2="18" y2="27"/></g>
    </svg>
  </div>
  <div class="service-tab is-grey" style="left:884px;width:281px">
    <span>SPEAK WITH A PATHOLOGIST</span>
    <svg width="16" height="30" viewBox="0 0 16 30" aria-hidden="true">
      <path d="M8 0L16 11H11V30H5V11H0z" fill="#fff"/>
    </svg>
  </div>

  <p class="service-copy" style="left:45px">Cras posuere, ipsum nec lobortis iaculis,Suspendisse aliquet est sit amet tellus dignissim facilisis. Aliqu</p>
  <p class="service-copy" style="left:333px">Cras posuere, ipsum nec lobortis iaculis, metus quam convalis eros, at suscipit ante orci.Lorem ipsum dolor sit amet, consectetur adipiscing elit. Aenean eget orci metus.</p>
  <p class="service-copy" style="left:617px">Cras posuere, ipsum nec lobortis iaculis, metus quam convalis eros, at suscipit ante orci.Lorem ipsum dolor sit amet, consectetur adipiscing elit. Aenean eget orci metus.</p>
  <p class="service-copy" style="left:898px">Cras posuere, ipsum nec lobortis iaculis, metus quam convalis eros, at suscipit ante orci.Lorem ipsum dolor sit amet, consectetur adipiscing elit. Aenean eget orci metus.</p>

  <div class="email-field">your email address</div>

  <a class="read-more is-green" href="#" style="left:199px;top:801px">READ MORE</a>
  <a class="read-more is-blue" href="#" style="left:476px;top:797px">READ MORE</a>
  <a class="read-more is-green" href="#" style="left:758px;top:800px">READ MORE</a>
  <a class="read-more is-blue" href="#" style="left:1053px;top:796px">READ MORE</a>

  <div class="footer-rule"></div>
  <div class="social-links" aria-label="Social links">
    <span style="background:var(--social-orange)"></span>
    <span style="background:var(--social-blue)"></span>
    <span style="background:var(--social-sky)"></span>
    <span style="background:var(--social-red)"></span>
    <span style="background:var(--social-cyan)"></span>
  </div>
</div>
</body>
</html>
```